Tour operator needs simple coded WordPress site (updated extra payment for coding and guaranteed)

[update 9/7/2015]
If you design a new logo and it gets accepted, even if we use another template with your logo you will get $50
[update 8/7/2015]
Update on questions about dual-language
For dual languages we are happy to set up a second site with the same designs in a second language.
For the design aspect just allow the user to switch between languages with an icon.
For the coding, a replica of the site on a second server will do (to save messing around with multiple language plugins) - we will populate it with Chinese text
[original post]
Simple coded WordPress site for tours
You can choose to design only or design and code ($340 design, $150 bonus for coding)
Open design brief - use your creativity
Will be in 2 languages (English and Chinese) but design needs only to be in one language
Winning design will be chosen only from home page, but the winner must make a second standard template page when chosen at no extra cost.
Must be responsive design
We only need homepage and standard template page design and coding, we will populate the pages
You can use design ideas from our pamphlet if you like - attached
Only a sample logo and colors on website and pamphlet - feel free to change as the current ones seem restrictive
Current website framework only to give an idea of the number of pages and basic menu structure (no need to use existing navigation style or any style at all for that matter, open brief)
http://brightwattlejourneys.com.au/
Target Market(s)
Chinese parents of kids 10-14 (the kids will take the tour)
Industry/Entity Type
Tour
Number of Pages Required
2 page
Look and feel
Each slider illustrates characteristics of the customer's brand and the style your logo design should communicate.

```html
<!DOCTYPE html>
<html lang="en">
<head>
<meta charset="utf-8">
<title>Bright Wattle Journeys</title>
<link href="https://fonts.googleapis.com/css2?family=Open+Sans:wght@400;600;700&display=swap" rel="stylesheet">
<style>
:root{
  --accent:#00b3d6;
  --ink:#333333;
  --muted:#555555;
  --green:#84a96a;
  --footer:#2e2e2e;
  --footer-line:#3d3d3d;
  --navy:#2c3e7a;
  --white:#ffffff;
}
*{margin:0;padding:0;box-sizing:border-box}
html,body{width:971px;height:1200px;overflow:hidden;background:var(--white)}
body{font-family:"Open Sans",Arial,sans-serif;color:var(--ink);position:relative}
.site-header{position:absolute;left:0;top:0;width:971px;height:86px}
.brand{position:absolute;left:80px;top:26px;display:flex;align-items:center;gap:8px;font-size:17px;font-weight:700;color:var(--navy)}
.brand-dot{width:22px;height:22px;border-radius:50%;background:#f2b705}
.lang{position:absolute;left:768px;top:18px;font-size:10.5px;color:var(--ink);display:flex;align-items:center;gap:8px}
.lang-flag{width:21px;height:13px;background:var(--navy)}
.main-nav{position:absolute;top:56px;left:586px;display:flex;font-size:11.5px}
.main-nav a{color:var(--ink);text-decoration:none;height:22px;line-height:22px;padding:0 12px}
.main-nav a.active{background:var(--accent);color:var(--white);width:66px;text-align:center;padding:0}
.hero{position:absolute;left:0;top:86px;width:971px;height:426px;background:linear-gradient(180deg,#5a3a8c 0%,#8a4f8e 40%,#c0705a 62%,#3d2c5a 80%,#2b2b4e 100%)}
.hero-arrow{position:absolute;top:280px;width:28px;height:28px;border-radius:50%;background:rgba(255,255,255,.55)}
.hero-arrow.prev{left:18px}.hero-arrow.next{left:926px;background:rgba(255,255,255,.25)}
.hero-caption{position:absolute;left:447px;top:304px;width:445px;height:80px;background:rgba(40,40,50,.6);color:var(--white);font-size:15.5px;font-weight:600;text-align:right;padding:20px 22px 0 20px;line-height:22px}
.hero-dots{position:absolute;top:409px;left:470px;display:flex;gap:7px}
.hero-dots span{width:6px;height:6px;border-radius:50%;background:var(--white)}
.hero-dots span.on{background:var(--accent)}
.about{position:absolute;left:80px;top:534px;width:534px}
.about h2{font-size:21px;font-weight:600;margin-bottom:13px}
.about .lead{font-size:11.5px;font-weight:600;line-height:15.5px;margin-bottom:24px}
.about p{font-size:8.8px;line-height:15.2px;color:var(--muted);margin-bottom:15px}
.btn{display:inline-block;margin-top:1px;width:96px;height:26px;line-height:26px;text-align:center;background:var(--accent);color:var(--white);font-size:10px;font-weight:600;text-decoration:none}
.safety{position:absolute;left:631px;top:539px;width:260px;height:295px;background:var(--green);color:var(--white);padding:10px 20px 0 21px}
.safety h3{font-size:21px;font-weight:400;margin-bottom:14px}
.safety ul{list-style:none}
.safety li{position:relative;padding-left:24px;font-size:10px;line-height:15.2px;margin-bottom:15px}
.safety li::before{content:"";position:absolute;left:3px;top:5px;width:5px;height:5px;border-radius:50%;background:var(--white)}
.gallery-title{position:absolute;left:78px;top:860px;font-size:21px;font-weight:600}
.gallery-nav{position:absolute;left:846px;top:861px}
.gallery{position:absolute;top:907px;left:79px;display:flex;gap:17px}
.gallery-item{width:190px;height:140px}
.g1{background:linear-gradient(160deg,#7fb7e0,#d7c9b0)}
.g2{background:linear-gradient(160deg,#4a8fd6,#7fb2e6)}
.g3{background:linear-gradient(160deg,#e0c58a,#cfc8c0)}
.g4{background:linear-gradient(160deg,#c9a98a,#3ba2a8)}
.site-footer{position:absolute;left:0;top:1112px;width:971px;height:88px;background:var(--footer)}
.footer-nav{position:absolute;top:0;left:0;width:971px;height:50px;border-bottom:1px solid var(--footer-line);display:flex;justify-content:center;align-items:center;gap:30px;padding-right:20px}
.footer-nav a{color:var(--white);font-size:11px;text-decoration:none}
.copyright{position:absolute;left:80px;top:61px;font-size:8.8px;color:var(--white)}
.social{position:absolute;left:831px;top:60px;display:flex;gap:8px}
.social span{width:14px;height:14px;border-radius:50%;background:var(--white)}
</style>
</head>
<body>
<header class="site-header">
  <div class="brand"><span class="brand-dot"></span>Bright Wattle Journeys</div>
  <div class="lang">Select Language: <span class="lang-flag"></span>
    <svg width="8" height="6" viewBox="0 0 8 6"><path d="M1 1l3 3 3-3" fill="none" stroke="#555" stroke-width="1"/></svg>
  </div>
  <nav class="main-nav">
    <a class="active" href="#">Home</a><a href="#">Travel insurance</a><a href="#">Contact</a><a href="#">About us</a>
  </nav>
</header>

<section class="hero" role="img" aria-label="Night city skyline with a lit suspension bridge over the bay at dusk">
  <span class="hero-arrow prev"></span><span class="hero-arrow next"></span>
  <div class="hero-caption">Learn about the unique wildlife and geography of this isolated continent</div>
  <div class="hero-dots"><span class="on"></span><span></span><span></span></div>
</section>

<section class="about">
  <h2>About</h2>
  <p class="lead">At the Bright Wattle Journeys we are passionate about educational travel and opportunities for students to gain academic and cultural understanding of Australia.</p>
  <p>14 day premium cultural and educational tours to Australian cities. Educational, safe, culturally enlightening and fun. Learn about educational institutions, history, sports, laws and customs, food and culture while improving your English. At the Bright Wattle Journeys we are passionate about educational travel and providing opportunities for students to learn more about a country and gain a deeper understanding of the culture. The out of classroom experience gained on our trips is invaluable. Planning and leading a Bright Wattle Journeys tour is easy because our team of dedicated experts assists every step of the way – from meticulously planning the curriculum to planning every detail of your trip, to accompanying you on tour.</p>
  <p>We inspect every hotel, visit every attraction, evaluate every teacher and sample every restaurant. Wherever you go on tour, we've been there. And we always listen to our travellers.</p>
  <a class="btn" href="#">Read More</a>
</section>

<aside class="safety">
  <h3>Safe and secure</h3>
  <ul>
    <li>Staff certified by the government for Working<br>With Children Staff certified in first aid care</li>
    <li>Professional accommodation with excellent history in</li>
    <li>caring for children with extremely well documented Safety Management Procedures including;</li>
    <li>Safety Management - reducing risk when taking students out of the classroom</li>
  </ul>
</aside>

<h2 class="gallery-title">Gallery</h2>
<svg class="gallery-nav" width="46" height="20" viewBox="0 0 46 20">
  <circle cx="10" cy="10" r="9" fill="none" stroke="#aaa" stroke-width="1.2"/>
  <path d="M15 10H6M9 7l-3 3 3 3" fill="none" stroke="#aaa" stroke-width="1.2"/>
  <circle cx="35" cy="10" r="9" fill="none" stroke="#333" stroke-width="1.2"/>
  <path d="M30 10h9M36 7l3 3-3 3" fill="none" stroke="#333" stroke-width="1.2"/>
</svg>
<div class="gallery">
  <div class="gallery-item g1" role="img" aria-label="Couple reading a map beside a canal"></div>
  <div class="gallery-item g2" role="img" aria-label="Traveller giving a thumbs up in front of a tower"></div>
  <div class="gallery-item g3" role="img" aria-label="Couple pointing at sights on a sunny street"></div>
  <div class="gallery-item g4" role="img" aria-label="Group of friends at a café terrace"></div>
</div>

<footer class="site-footer">
  <nav class="footer-nav"><a href="#">Home</a><a href="#">Travel insurance</a><a href="#">Contact</a><a href="#">About us</a></nav>
  <div class="copyright">© 2015 Yoursite, All rights reserved.</div>
  <div class="social"><span></span><span></span><span></span></div>
</footer>
</body>
</html>
```